Business Card Design Project

Use our current logo. Clean design.

Industry/Entity Type

Business

Requirements
Must have
• Marisela DUBRANCQ
M. Law
Managing Partner

Alpenvorsa AG
Kornhalmweg 214
CH-3097 Liebefeld

M. +41 79 412 56 27
T. +41 31 928 44 10
F. +41 31 928 44 19

m.dubrancq@alpenvorsa-example.com
www.alpenvorsa-example.com

```html
<!DOCTYPE html>
<html lang="en">
<head>
<meta charset="utf-8">
<title>Alpenvorsa AG – Business Card</title>
<link rel="stylesheet" href="https://fonts.googleapis.com/css2?family=Tenor+Sans&display=swap">
<style>
  :root {
    --stage: #2a2a2a;
    --card-dark: #2b2626;
    --card-light: #ffffff;
    --ink-dark: #1d1d1d;
    --ink-light: #f4f4f4;
    --rule: #6a6a6a;
  }
  * { margin: 0; padding: 0; box-sizing: border-box; }
  html, body {
    width: 1200px; height: 900px; overflow: hidden;
    background: var(--stage);
    font-family: "Tenor Sans", sans-serif;
  }
  .stage {
    position: relative; width: 1200px; height: 900px;
    display: flex; justify-content: center; align-items: center; gap: 40px;
  }
  .card {
    width: 300px; height: 520px; border-radius: 28px;
    position: relative;
    box-shadow: 0 14px 30px rgba(0,0,0,.45);
  }
  .card--front { background: var(--card-dark); color: var(--ink-light); }
  .card--back { background: var(--card-light); color: var(--ink-dark); text-align: center; }

  .brand { display: flex; flex-direction: column; align-items: center; }
  .brand__mark { width: 14px; height: 14px; background: currentColor; margin-bottom: 10px; }
  .brand__name { letter-spacing: .06em; text-transform: uppercase; }

  .card--front .brand { position: absolute; top: 185px; left: 0; right: 0; }
  .card--front .brand__mark { width: 22px; height: 22px; margin-bottom: 16px; }
  .card--front .brand__name { font-size: 30px; }
  .card--front .web {
    position: absolute; bottom: 62px; left: 0; right: 0;
    text-align: center; font-size: 13px; letter-spacing: .02em;
  }

  .card--back .brand { padding-top: 56px; }
  .card--back .brand__name { font-size: 15px; }
  .company { margin-top: 10px; font-size: 14px; line-height: 1.05; }
  .company__name { font-size: 15px; }

  .person { margin-top: 62px; }
  .person__name { font-size: 17px; letter-spacing: .03em; }
  .person__role { font-size: 13px; line-height: 1.05; }

  .rule { height: 1px; background: var(--rule); margin: 8px 40px; }

  .contact { font-size: 14px; line-height: 1.05; }
  .contact__label { font-size: 8px; letter-spacing: .06em; text-transform: uppercase; display: block; }
  .contact__value { display: block; margin-bottom: 2px; }

  .online { font-size: 14px; line-height: 1.15; }
</style>
</head>
<body>
  <main class="stage">
    <section class="card card--front" aria-label="Card front">
      <div class="brand">
        <span class="brand__mark"></span>
        <span class="brand__name">Alpenvorsa</span>
      </div>
      <p class="web">www.alpenvorsa-example.com</p>
    </section>

    <section class="card card--back" aria-label="Card back">
      <div class="brand">
        <span class="brand__mark"></span>
        <span class="brand__name">Alpenvorsa</span>
      </div>
      <address class="company" style="font-style:normal">
        <div class="company__name">Alpenvorsa AG</div>
        <div>Kornhalmweg 214</div>
        <div>CH-3097 Liebefeld</div>
      </address>

      <div class="person">
        <div class="person__name">MARISELA DUBRANCQ</div>
        <div class="person__role">M. Law</div>
        <div class="person__role">Managing Partner</div>
      </div>

      <div class="rule"></div>

      <div class="contact">
        <span class="contact__label">Mobile:</span>
        <span class="contact__value">+41 79 412 56 27</span>
        <span class="contact__label">Telephone:</span>
        <span class="contact__value">+41 31 928 44 10</span>
        <span class="contact__label">Fax:</span>
        <span class="contact__value">+41 31 928 44 19</span>
      </div>

      <div class="rule"></div>

      <div class="online">
        <div>m.dubrancq@alpenvorsa-example.com</div>
        <div>www.alpenvorsa-example.com</div>
      </div>
    </section>
  </main>
</body>
</html>
```